Buff & Gleam

polished concrete and epoxy coatings flooring company

Target Market(s)

Industrial commercial

Industry/Entity Type

Industrial flooring contractor

Contact Information for Business Card

POLISHED CONCRETE • EPOXY COATING • TERRAZZO RESTORATION • SHOT BLASTING • SURFACE PREPARATION • JOINT FILLING • TILE/ CARPET /GLUE REMOVAL

Colors
0054AA
0677BA
7BADD7
CADEEF
E8F1F8

Requirements
Must have
• email buffandgleamfloors@mailbrook.example Address 47215 Tallowmere Rd, Fraser, MI 48093. Name Ray Tulvin. Services Polished concrete- Epoxy Coatings- Terrazzo restoration-surface preparation- safety striping- joint filling- tile/ carpet/ glue removal phone number 586-700-3926 email buffandgleamfloors.example
Nice to have
• Instagram Facebook logo maybe smaller in the corner

```html
<!DOCTYPE html>
<html lang="en">
<head>
<meta charset="utf-8">
<title>Buff &amp; Gleam – Business Card</title>
<link rel="stylesheet" href="https://fonts.googleapis.com/css2?family=Montserrat:wght@400;500;700&display=swap">
<style>
  :root {
    --backdrop: #bdbdbd;
    --blue-deep: #0054AA;
    --blue-mid: #0677BA;
    --blue-soft: #7BADD7;
    --blue-pale: #CADEEF;
    --blue-mist: #E8F1F8;
    --ink: #0b2747;
    --text-light: #ffffff;
    --shadow: rgba(0, 0, 0, 0.35);
  }
  * { box-sizing: border-box; margin: 0; padding: 0; }
  html, body {
    width: 1200px; height: 1200px; overflow: hidden;
    background: var(--backdrop);
    font-family: "Montserrat", sans-serif;
  }
  .canvas { position: relative; width: 1200px; height: 1200px; }

  .card {
    position: absolute; left: 150px; width: 898px; height: 524px;
    background: var(--blue-deep);
    box-shadow: 0 8px 18px var(--shadow);
  }
  .card--front { top: 55px; }
  .card--back { top: 620px; }

  .info-panel {
    position: absolute; left: 184px; top: 70px; width: 661px; height: 385px;
    background: var(--blue-pale);
  }

  .brand-frame {
    position: absolute; left: 72px; top: 130px; width: 305px; height: 265px;
    background: var(--blue-deep);
  }
  .brand-block {
    position: absolute;
    display: flex; align-items: center; justify-content: center;
  }
  .brand-block--front { left: 72px; top: 141px; width: 287px; height: 244px; }
  .brand-block--back { left: 500px; top: 126px; width: 322px; height: 274px; }
  .brand-texture {
    position: absolute; inset: 0;
    background: radial-gradient(circle at 45% 40%, var(--blue-mist), var(--blue-soft));
  }
  .brand-name {
    position: relative;
    font-weight: 700; color: var(--blue-deep);
    text-transform: uppercase; text-align: center; line-height: 1.1;
  }
  .brand-block--front .brand-name { font-size: 40px; }
  .brand-block--back .brand-name { font-size: 45px; }

  .person-name {
    position: absolute; left: 421px; top: 110px;
    font-size: 35px; font-weight: 700; color: var(--blue-deep); letter-spacing: 0.5px;
  }
  .person-role {
    position: absolute; left: 421px; top: 155px;
    font-size: 23px; font-weight: 400; color: var(--blue-mid);
  }

  .contact-list { position: absolute; left: 421px; top: 216px; list-style: none; }
  .contact-list li {
    display: flex; align-items: center; height: 34.5px;
    font-size: 20px; color: var(--ink); white-space: nowrap;
  }
  .contact-list li.contact-web { margin-top: 18px; }
  .contact-list svg { width: 18px; height: 18px; margin-right: 12px; flex: none; }
  .contact-list svg .ico { fill: var(--blue-deep); }
  .contact-list svg .ico-line { fill: none; stroke: var(--blue-deep); }
  .contact-list .mail, .contact-list .addr { font-size: 17.5px; }

  .service-list {
    position: absolute; left: 85px; top: 134px; list-style: none;
  }
  .service-list li {
    height: 32px; font-size: 20px; font-weight: 500;
    color: var(--text-light); letter-spacing: 0.3px; white-space: nowrap;
  }
  .service-list li::before { content: "•"; margin-right: 6px; color: var(--blue-pale); }
</style>
</head>
<body>
<main class="canvas">

  <section class="card card--front">
    <div class="info-panel"></div>
    <div class="brand-frame"></div>
    <div class="brand-block brand-block--front">
      <div class="brand-texture" role="img" aria-label="Polished concrete texture behind the company name"></div>
      <p class="brand-name">Buff &amp;<br>Gleam</p>
    </div>

    <h1 class="person-name">RAY TULVIN</h1>
    <p class="person-role">Manager</p>

    <ul class="contact-list">
      <li>
        <svg viewBox="0 0 24 24"><rect class="ico-line" x="6" y="2" width="12" height="20" rx="2" stroke-width="2.4"/><circle class="ico" cx="12" cy="18" r="1.3"/></svg>
        586-700-3926
      </li>
      <li>
        <svg viewBox="0 0 24 24"><path class="ico" d="M6.6 10.8a15 15 0 0 0 6.6 6.6l2.2-2.2a1 1 0 0 1 1-.25 11.4 11.4 0 0 0 3.6.57 1 1 0 0 1 1 1V20a1 1 0 0 1-1 1A17 17 0 0 1 3 4a1 1 0 0 1 1-1h3.5a1 1 0 0 1 1 1c0 1.25.2 2.45.57 3.57a1 1 0 0 1-.25 1z"/></svg>
        586-700-3927
      </li>
      <li class="mail">
        <svg viewBox="0 0 24 24"><path class="ico" d="M3 5h18v14H3z"/><path d="M3 6l9 6 9-6" fill="none" stroke="#CADEEF" stroke-width="1.8"/></svg>
        buffandgleamfloors@mailbrook.example
      </li>
      <li class="addr">
        <svg viewBox="0 0 24 24"><path class="ico" d="M12 2a7 7 0 0 0-7 7c0 5.2 7 13 7 13s7-7.8 7-13a7 7 0 0 0-7-7zm0 9.5A2.5 2.5 0 1 1 12 6.5a2.5 2.5 0 0 1 0 5z"/></svg>
        47215 Tallowmere Rd, Fraser, MI 48093
      </li>
      <li class="contact-web">
        <svg viewBox="0 0 24 24"><circle class="ico-line" cx="12" cy="12" r="9" stroke-width="2"/><path class="ico-line" d="M3 12h18M12 3c3 3 3 15 0 18M12 3c-3 3-3 15 0 18" stroke-width="1.6"/></svg>
        buffandgleamfloors.example
      </li>
    </ul>
  </section>

  <section class="card card--back">
    <ul class="service-list">
      <li>POLISHED CONCRETE</li>
      <li>EPOXY COATING</li>
      <li>TERRAZZO RESTORATION</li>
      <li>SHOT BLASTING</li>
      <li>SURFACE PREPARATION</li>
      <li>SAFETY STRIPING</li>
      <li>JOINT FILLING</li>
      <li>TILE/ CARPET /GLUE REMOVAL</li>
    </ul>
    <div class="brand-block brand-block--back">
      <div class="brand-texture" role="img" aria-label="Polished concrete texture behind the company name"></div>
      <p class="brand-name">Buff &amp;<br>Gleam</p>
    </div>
  </section>

</main>
</body>
</html>
```